Web Design Project

Psychotherapist in Private Practice
Practice name "The Quiet Harbour"
The population is professional adults seeking life coaching and change consultation
I am including a photo for inspiration ONLY - It includes the theme of light and tree branches. There does not HAVE to be a photograph . An illustration , concept or theme of nature /light / generativity / growth / creativity is acceptable
Clean sharp lines Light colors, minimalist , modern.
There is a separate project for a logo design that will become part of the web design
Here are examples of two logos/websites I like
http://www.brightmeadowcentre.ca/
http://www.openridgeadvisors.ca/

Target Market(s)

Professional adults seeking life coaching

Industry/Entity Type

Life Coaching

Requirements
Should not have
• Although the business name has 'compassion' in it, designs with hearts in it would have to be pretty stylish, subtle, mature and sophisticated to be considered.

```html
<!DOCTYPE html>
<html lang="en">
<head>
<meta charset="utf-8">
<title>The Quiet Harbour</title>
<link href="https://fonts.googleapis.com/css2?family=Ubuntu:wght@400;500;700&display=swap" rel="stylesheet">
<style>
:root{
  --green:#1a8a4f;
  --green-dark:#146e3e;
  --green-text:#2a7f2a;
  --olive:#6b5413;
  --heading:#444;
  --body:#444;
  --link:#2f8fc4;
  --rule:#cfe0d6;
  --bg-top:#eef5ef;
  --bg-bottom:#dfeee3;
}
*{box-sizing:border-box;margin:0;padding:0}
html,body{width:1200px;height:1142px;overflow:hidden}
body{font-family:"Ubuntu",sans-serif;color:var(--body);background:linear-gradient(135deg,#f6faf6 0%,var(--bg-top) 50%,var(--bg-bottom) 100%);position:relative}
.abs{position:absolute}
.brand{left:78px;top:26px;display:flex;align-items:center;gap:12px}
.brand-mark{width:44px;height:44px;border-radius:50%;background:#8fb86a}
.brand-name{font-size:34px;font-weight:500;color:var(--green-text)}
.help{left:612px;top:38px;width:240px;text-align:center}
.help .ask{font-size:14px;font-weight:500;color:var(--olive)}
.help .phone{font-size:20px;font-weight:500;color:var(--green-dark);margin-top:4px}
.textsize{left:996px;top:12px;display:flex;align-items:flex-end;gap:6px;font-size:13px;color:#888}
.textsize b{color:var(--green);font-weight:400}
.search{left:874px;top:46px;width:196px;height:31px;border:1px solid #d6ddd8;background:#fff;border-radius:3px;font-size:13px;font-style:italic;color:#777;padding:7px 14px}
.search-btn{left:1081px;top:46px;width:40px;height:31px;border-radius:6px;background:var(--green)}
.nav{left:0;top:105px;height:43px;width:1200px}
.tab{position:absolute;top:0;height:43px;background:var(--green);color:#fff;font-size:13px;font-weight:500;display:flex;align-items:center;justify-content:center;border-radius:6px 6px 0 0;letter-spacing:.2px}
.tab.active{background:#fff;color:var(--green);border:1px solid var(--green);border-bottom:none;height:44px;font-size:14px}
.panel{left:76px;top:147px;width:1048px;height:854px;background:#fff;border:1px solid var(--green);border-radius:0 6px 8px 8px}
.slider{left:99px;top:180px;width:731px;height:321px;border-radius:8px;overflow:hidden;border:1px solid #ccc;background:linear-gradient(180deg,#f4d24a 0%,#fbeeb0 38%,#f6a64b 62%,#5a5b63 68%,#3e3f46 100%)}
.slider .caption{position:absolute;left:0;top:240px;width:100%;height:81px;background:rgba(40,40,40,.72);padding:8px 24px;color:#fff}
.caption h2{font-size:28px;font-weight:500}
.caption p{font-size:19px;margin-top:2px}
.arrow{position:absolute;top:270px;width:30px;height:30px;border-radius:50%;background:#8c8c8c}
.welcome{left:99px;top:524px;font-size:25px;font-weight:500;color:#555}
.welcome span{color:var(--green)}
.dots{left:99px;top:562px;width:720px;border-top:2px dotted #ddd}
.intro{left:99px;top:574px;width:722px;font-size:12.6px;line-height:20px;color:#444}
.side{left:858px;width:254px}
.side h3{font-size:19px;font-weight:500;color:#444}
.side h3 span{color:var(--green-text)}
.side .lead{color:var(--green-text);font-size:14px;line-height:20px}
.side small{font-size:11.5px;line-height:20px;color:#555}
.side-rule{left:858px;width:254px;border-top:1px solid #ddd}
.doctor{left:975px;top:165px;width:138px;height:156px;background:linear-gradient(180deg,#f4f6f8,#d9e4ee)}
.col{top:782px;height:218px;border-left:1px solid var(--rule)}
.col-title{display:flex;align-items:center;gap:14px;font-size:19px;font-weight:500;color:#2b6a2b}
.sq{width:33px;height:33px;border-radius:5px}
.col p{font-size:12px;line-height:18px;color:#333}
.meta{font-size:11px;color:var(--link)}
.ul{color:var(--link);font-size:13px;border-bottom:1px dotted var(--link);padding-bottom:2px}
.footer{left:76px;top:1016px;width:1046px;height:102px;border-radius:6px;background:linear-gradient(180deg,#1a9a58,#138148);color:#e6f4ea}
.ficon{width:22px;height:22px;border-radius:3px;display:inline-block;margin-right:10px}
</style>
</head>
<body>

<div class="abs brand"><span class="brand-mark"></span><span class="brand-name">The Quiet Harbour</span></div>

<div class="abs help"><div class="ask">Find Out How We Can Help You</div><div class="phone">123-456-789</div></div>

<div class="abs textsize">
  <svg width="12" height="18" viewBox="0 0 12 18"><rect x="1" y="1" width="10" height="16" rx="2" fill="#555"/><rect x="3" y="3" width="6" height="10" fill="#ddd"/></svg>
  Text size <b style="font-size:13px">A</b><b style="font-size:16px">A</b><b style="font-size:20px">A</b>
</div>
<div class="abs search">Search..</div>
<div class="abs search-btn">
  <svg width="40" height="31" viewBox="0 0 40 31"><circle cx="17" cy="13" r="6" fill="none" stroke="#fff" stroke-width="3"/><line x1="21.5" y1="17.5" x2="28" y2="24" stroke="#fff" stroke-width="4" stroke-linecap="round"/></svg>
</div>

<nav class="abs nav">
  <div class="tab active" style="left:87px;width:81px">Home</div>
  <div class="tab" style="left:172px;width:174px">Evidence We Can Help</div>
  <div class="tab" style="left:349px;width:124px">Meet Our Team</div>
  <div class="tab" style="left:476px;width:149px">Therapy &amp; Training</div>
  <div class="tab" style="left:628px;width:100px">Multimedia</div>
  <div class="tab" style="left:731px;width:135px">For Professional</div>
  <div class="tab" style="left:869px;width:135px">Schedule &amp; Fees</div>
  <div class="tab" style="left:1007px;width:100px">Contact Us</div>
</nav>

<div class="abs panel"></div>

<div class="abs slider" role="img" aria-label="Sunset over the sea framed by overhanging tree branches">
  <div class="caption"><h2>Slider Headinf Goes Here</h2><p>Lorem ipsum dolor sit amet, consect- etuer adipiscing elit..</p></div>
  <div class="arrow" style="left:639px"><svg width="30" height="30"><path d="M18 8 L10 15 L18 22 M10 15 H22" stroke="#444" stroke-width="3" fill="none"/></svg></div>
  <div class="arrow" style="left:686px"><svg width="30" height="30"><path d="M12 8 L20 15 L12 22 M20 15 H8" stroke="#444" stroke-width="3" fill="none"/></svg></div>
</div>

<h1 class="abs welcome">Welcome to <span>the Quiet Harbour..</span></h1>
<div class="abs dots"></div>
<div class="abs intro">
  Lorem ipsum dolor sit amet, consectetur adipisicing elit, sed do eiusmod tempor incididunt ut labore et dolore magna aliqua.<br>
  Ut enim ad minim veniam, quis nostrud exercitation ullamco laboris nisi ut aliquip<br>
  ex ea commodo consequat.<br>
  Duis aute irure dolor in reprehenderit in voluptate velit esse cillum dolore eu fugiat nulla pariatur. Excepteur sint occaecat cupidatat non proident, sunt in culpa qui officia deserunt mollit anim id est laborum.<br>
  sint occaecat cupidatat non proident, sunt in culpa qui officia. Aliquam molestie, mi et imperdiet euismod, dui purus auctor tellus, et interdum lacus lectus et ante. Sed accumsan sollicitudin sapien, sit amet adipiscing turpis gravida ac. In congue, neque ac lobortis volutpat, libero mauris varius mi, vitae suscipit ipsum ligula vitae risus.
</div>

<div class="abs doctor" role="img" aria-label="Portrait of the practice doctor in a white coat"></div>
<div class="abs side" style="top:176px;width:130px">
  <h3 style="color:var(--olive)">Ask Dr. Ellison</h3>
  <div class="lead" style="margin-top:4px">Can DBT Help My Teenager?</div>
  <small>Do you have a question about mindfulness?</small>
  <div style="font-size:12px;font-weight:500;color:var(--olive);margin-top:2px">Ask Now <span style="color:var(--green)">»</span></div>
</div>
<div class="abs side-rule" style="top:331px"></div>

<div class="abs side" style="top:343px">
  <h3>Upcoming <span>Workshop</span></h3>
  <div style="margin-top:8px;line-height:20px"><span class="lead">Duis aute irure dolor</span> <small>in reprehenderit in voluptate velit esse cillum dolore eu fugiat nulla pariatur. Excep...</small></div>
  <div style="font-size:11px;font-weight:500;color:var(--olive);margin-top:12px">May 25, 2013</div>
</div>
<div class="abs side-rule" style="top:483px"></div>

<div class="abs side" style="top:503px">
  <h3>Blog <span>Posts</span></h3>
  <div class="lead" style="font-weight:500;margin-top:10px">Duis aute irure dolorisus in magna varius commodo.</div>
  <div style="font-size:12px;color:var(--olive);margin-top:8px">Read this post &nbsp;<span style="color:#aaa">|</span>&nbsp; See all posts</div>
</div>
<div class="abs side-rule" style="top:624px"></div>

<div class="abs side" style="top:645px">
  <h3 style="color:#2b5a2b">2013 Calender</h3>
  <div style="display:flex;gap:14px;margin-top:8px">
    <svg width="47" height="47" viewBox="0 0 47 47"><rect x="1" y="4" width="45" height="42" rx="3" fill="#fff" stroke="#888"/><rect x="1" y="4" width="45" height="10" fill="#c9302c"/><g stroke="#bbb"><line x1="5" y1="22" x2="42" y2="22"/><line x1="5" y1="30" x2="42" y2="30"/><line x1="5" y1="38" x2="42" y2="38"/><line x1="14" y1="17" x2="14" y2="43"/><line x1="23" y1="17" x2="23" y2="43"/><line x1="32" y1="17" x2="32" y2="43"/></g></svg>
    <div style="font-size:13px;line-height:20px;color:#333">See our Calendar of Courses &amp; Events</div>
  </div>
</div>

<div class="abs" style="left:142px;top:770px;width:914px;border-top:1px solid #ddd"></div>

<div class="abs" style="left:150px;top:800px;width:195px">
  <div class="col-title"><span class="sq" style="background:#5bc0e8"></span>Chatter</div>
  <p style="margin-top:20px">Lorem Ipsum is simply dummy text of the printing &amp; typsetting indus-tryaute irure dolor.</p>
  <div class="meta" style="margin-top:16px">03:50 PM Jun 03 <span style="color:#999;margin-left:14px">↶ &nbsp; ⇄ &nbsp; ☆</span></div>
  <div style="margin-top:16px"><span class="ul">Follow us</span></div>
</div>

<div class="abs col" style="left:360px;width:240px"></div>
<div class="abs" style="left:381px;top:800px;width:210px">
  <div class="col-title"><span class="sq" style="background:#3b5a9a"></span>Circlebook</div>
  <div style="display:flex;gap:20px;margin-top:24px">
    <div role="img" aria-label="Profile photo of a commenter" style="width:58px;height:58px;border:1px solid #e0b43a;background:linear-gradient(180deg,#e7d8c8,#6b4a3a);flex:none"></div>
    <div>
      <div class="meta" style="color:var(--olive)">03 JUN 2013</div>
      <p>Lorem Ipsum is simply dummy text dolor.</p>
      <div style="display:inline-block;margin-top:6px;font-size:9px;border:1px solid #aab;padding:1px 4px;border-radius:2px;background:#eef">Like</div>
      <div style="margin-top:18px"><span class="ul">Read more</span></div>
    </div>
  </div>
</div>

<div class="abs col" style="left:600px;width:240px"></div>
<div class="abs" style="left:623px;top:800px;width:200px">
  <div class="col-title"><svg width="34" height="28" viewBox="0 0 34 28"><rect x="1" y="4" width="32" height="22" fill="#f4f4f4" stroke="#aaa"/><path d="M1 4 L17 17 L33 4" fill="none" stroke="#aaa"/></svg>Stay in Touch</div>
  <div style="margin-top:24px;width:175px;height:26px;border:1px solid #ddd;border-radius:2px;font-size:11px;font-style:italic;color:#888;padding:6px 11px">Enter your Email...</div>
  <div style="margin-top:12px;width:82px;height:26px;background:linear-gradient(#2d8a34,#1c6a22);color:#fff;font-size:12px;font-weight:500;text-align:center;line-height:26px">Sign Up</div>
</div>

<div class="abs col" style="left:840px;width:1px"></div>
<div class="abs" style="left:862px;top:800px;width:220px">
  <div class="col-title"><svg width="36" height="30" viewBox="0 0 36 30"><path d="M2 2 H34 V22 H16 L8 29 V22 H2 Z" fill="#f8f8f8" stroke="#bbb"/></svg>Share this Site</div>
  <div style="font-size:14px;color:#333;margin-top:22px">Like our website?</div>
  <div style="margin-top:6px"><span class="ul" style="font-size:14px">Tell a friend about us</span></div>
</div>

<footer class="abs footer">
  <div class="abs" style="left:19px;top:20px">
    <span class="ficon" style="background:#5bc0e8"></span><span class="ficon" style="background:#3b5a9a"></span><span class="ficon" style="background:#d62a1e"></span><span class="ficon" style="background:#e6b323"></span><span class="ficon" style="background:#e8e8e8"></span><span class="ficon" style="background:#f08a1c"></span>
  </div>
  <div class="abs" style="left:18px;top:62px;font-size:12px">© 2013 the Quiet Harbour. All Right Reserved.</div>
  <div class="abs" style="left:420px;top:28px;width:180px;text-align:right;font-size:17px;font-weight:500;line-height:24px">416-555-0142<br>1-866-555-0199</div>
  <div class="abs" style="left:715px;top:28px;font-size:14px;font-weight:500;line-height:25px">info@thequietharbour.com<br>1200 Alder Lane, Harbourview, H02 47QT.</div>
</footer>

</body>
</html>
```